Lantern Business Cards

Need business cards for my employees at my restaurant.

Needs to include:
Our Logo
Lantern Bowls & Brews
Name: Nora Pettigrew
Title : Owner
Address: 487 Mirella Ave. Lake Havasu City, AZ 86519
Web: www.lanternkestrel.com
Phone: 928-555-0147
Cell: 928-555-0192
Email: info@lanternkestrel.com

```html
<!DOCTYPE html>
<html lang="en">
<head>
<meta charset="utf-8">
<title>Lantern Bowls &amp; Brews — Business Card</title>
<link href="https://fonts.googleapis.com/css2?family=Montserrat:wght@500;700&family=Arimo:wght@700&family=Lato:wght@400&family=Open+Sans:ital,wght@1,400&display=swap" rel="stylesheet">
<style>
  :root{
    --red:#b81f2e;
    --red-deep:#7a0f1e;
    --band-red:#ad1c2b;
    --ink:#0b0b0c;
    --glow:#4a4a4c;
    --white:#ffffff;
    --page:#ffffff;
    --rule-dark:#333333;
  }
  html,body{margin:0;padding:0;overflow:hidden;background:var(--page);}
  .canvas{position:relative;width:1200px;height:1200px;overflow:hidden;background:var(--page);}
  .card{position:absolute;width:722px;height:388px;overflow:hidden;box-shadow:4px 5px 6px rgba(0,0,0,.45);}

  /* front */
  .card--front{left:246px;top:164px;
    background:radial-gradient(ellipse 52% 56% at 50% 48%, var(--red-deep) 0%, #9c1626 55%, var(--red) 100%);}
  .front-mark{position:absolute;left:50%;top:92px;transform:translateX(-50%);
    width:112px;height:112px;border-radius:50%;background:var(--white);}
  .front-name{position:absolute;left:0;right:0;top:222px;text-align:center;
    font-family:"Montserrat",sans-serif;font-weight:700;font-size:60px;letter-spacing:2px;
    color:var(--white);text-transform:uppercase;line-height:1;}
  .front-tagline{position:absolute;left:194px;width:334px;top:279px;
    display:flex;align-items:center;gap:14px;
    font-family:"Montserrat",sans-serif;font-weight:500;font-size:14px;letter-spacing:1.5px;
    color:var(--white);text-transform:uppercase;white-space:nowrap;line-height:1;}
  .front-tagline::before,.front-tagline::after{content:"";flex:1;height:2px;background:var(--white);}

  /* back */
  .card--back{left:251px;top:594px;
    background:
      radial-gradient(ellipse 40% 60% at 48% 100%, var(--glow) 0%, rgba(0,0,0,0) 100%) top/100% 141px no-repeat,
      radial-gradient(ellipse 40% 60% at 48% 0%, var(--glow) 0%, rgba(0,0,0,0) 100%) bottom/100% 133px no-repeat,
      var(--ink);}
  .contact-row{position:absolute;left:0;right:0;top:60px;text-align:center;
    font-family:"Arimo",sans-serif;font-weight:700;font-size:24px;color:var(--white);white-space:nowrap;}
  .contact-row .label{color:var(--red);}
  .contact-row .gap{display:inline-block;width:32px;}

  .band{position:absolute;left:0;top:141px;width:722px;height:114px;}
  .band svg{position:absolute;left:0;top:0;}
  .band-mark{position:absolute;left:28px;top:22px;width:70px;height:70px;border-radius:50%;background:var(--red);}
  .band-name{position:absolute;left:111px;top:30px;width:186px;text-align:center;
    font-family:"Montserrat",sans-serif;font-weight:700;font-size:34px;color:var(--red);
    text-transform:uppercase;letter-spacing:1px;line-height:1;}
  .band-tagline{position:absolute;left:111px;width:186px;top:64px;
    display:flex;align-items:center;gap:6px;
    font-family:"Montserrat",sans-serif;font-weight:500;font-size:9px;letter-spacing:.6px;
    color:var(--rule-dark);text-transform:uppercase;white-space:nowrap;line-height:1;}
  .band-tagline::before,.band-tagline::after{content:"";flex:1;height:1px;background:var(--rule-dark);}
  .person{position:absolute;left:360px;width:300px;top:28px;text-align:center;color:var(--white);}
  .person-name{font-family:"Lato",sans-serif;font-weight:400;font-size:36px;line-height:1;}
  .person-title{font-family:"Open Sans",sans-serif;font-style:italic;font-size:20px;margin-top:2px;}

  .detail{position:absolute;font-family:"Open Sans",sans-serif;font-style:italic;font-size:18px;color:var(--white);white-space:nowrap;}
  .detail svg{position:absolute;}
  .detail--email{left:117px;top:293px;}
  .detail--email svg{left:-52px;top:2px;}
  .detail--web{left:447px;top:283px;}
  .detail--web svg{left:-44px;top:-1px;}
  .detail--address{left:0;right:0;top:340px;text-align:center;}
</style>
</head>
<body>
<div class="canvas">

  <section class="card card--front" aria-label="Card front">
    <div class="front-mark"></div>
    <div class="front-name">Lantern</div>
    <div class="front-tagline">Bowls and Brews</div>
  </section>

  <section class="card card--back" aria-label="Card back">
    <div class="contact-row">
      <span class="label">Phone NO.</span> 928-555-0147<span class="gap"></span><span class="label">Cell NO.</span> 928-555-0192
    </div>

    <div class="band">
      <svg width="722" height="114" viewBox="0 0 722 114">
        <rect width="722" height="114" fill="var(--band-red)"/>
        <polygon points="0,0 386,0 271,114 0,114" fill="var(--white)"/>
      </svg>
      <div class="band-mark"></div>
      <div class="band-name">Lantern</div>
      <div class="band-tagline">Bowls and Brews</div>
      <div class="person">
        <div class="person-name">Nora Pettigrew</div>
        <div class="person-title">Owner</div>
      </div>
    </div>

    <div class="detail detail--email">
      <svg width="34" height="22" viewBox="0 0 34 22"><rect x="0" y="0" width="34" height="22" fill="var(--red)"/><polyline points="0,0 17,13 34,0" fill="none" stroke="var(--ink)" stroke-width="2"/><polyline points="0,22 13,10 M34,22 21,10" fill="none" stroke="var(--ink)" stroke-width="2"/></svg>
      info@lanternkestrel.com
    </div>

    <div class="detail detail--web">
      <svg width="30" height="30" viewBox="0 0 30 30"><circle cx="15" cy="15" r="14" fill="var(--red)"/><ellipse cx="15" cy="15" rx="6" ry="14" fill="none" stroke="var(--ink)" stroke-width="1.6"/><line x1="1" y1="15" x2="29" y2="15" stroke="var(--ink)" stroke-width="1.6"/></svg>
      www.lanternkestrel.com
    </div>

    <div class="detail detail--address">487 Mirella Ave. Lake Havasu City, AZ 86519</div>
  </section>

</div>
</body>
</html>
```